Brindle Harbor Stationery Design Project

We need complete stationary design for a start up company called "Brindle Harbor". We develop B2B and B2C SAAS based solutions and e-commerce portals for companies. The design should communicate simplicity and elegance. The domain name of the site will be brindleharbor.com. The logo of the company is https://files.quellbox.net/u/4817205/7734_2208615_91437_image.jpg
Updates

Target Market(s)

B2B and B2C

Industry/Entity Type

E-Commerce

Requirements
Must have
• The design should reflect the followings:
- Company logo
- Company activities
- Be modern
Nice to have
• Preferably, the colors of the logo are to be used, but we are open for suggestions.

A design with transparent background might be nice.

```html
<!DOCTYPE html>
<html lang="en">
<head>
<meta charset="utf-8">
<title>Brindle Harbor — Business Cards</title>
<link href="https://fonts.googleapis.com/css2?family=Open+Sans:wght@400;600;700&display=swap" rel="stylesheet">
<style>
  :root {
    --backdrop: #1a1917;
    --card-white: #ffffff;
    --card-grey: #d9dadb;
    --brand-red: #d42a3c;
    --brand-blue: #1f6cb3;
    --text-grey: #5f6063;
    --divider: #8a8b8d;
  }
  * { box-sizing: border-box; margin: 0; padding: 0; }
  html, body {
    width: 1200px; height: 901px; overflow: hidden;
    background: var(--backdrop);
    font-family: "Open Sans", Arial, sans-serif;
  }
  .stage {
    width: 1200px; height: 901px;
    display: flex; flex-direction: column;
    align-items: center; justify-content: center; gap: 40px;
  }
  .business-card {
    width: 620px; height: 354px;
    display: flex; align-items: center; justify-content: center;
    gap: 22px;
  }
  .business-card--front { background: var(--card-white); }
  .business-card--back { background: var(--card-grey); }

  .brand-block { display: flex; flex-direction: column; align-items: flex-end; }
  .brand-name {
    display: flex; align-items: center; gap: 8px;
    font-weight: 700; font-size: 25px; color: var(--brand-blue);
    letter-spacing: -0.3px;
    padding-bottom: 6px;
    border-bottom: 2px solid var(--brand-blue);
  }
  .brand-dot {
    width: 14px; height: 14px; border-radius: 50%;
    background: var(--brand-red);
  }
  .tagline {
    margin-top: 10px;
    text-align: right;
    font-size: 11.5px; font-weight: 700; line-height: 1.35;
    color: var(--text-grey);
  }
  .divider { width: 2px; height: 96px; background: var(--divider); }

  .contact-block { display: flex; flex-direction: column; }
  .person-name { font-size: 13px; font-weight: 700; color: var(--text-grey); }
  .accent-lines { margin: 6px 0 10px; width: 72px; }
  .accent-lines span { display: block; height: 2px; }
  .accent-lines .red { background: var(--brand-red); margin-bottom: 4px; }
  .accent-lines .blue { background: var(--brand-blue); }
  .contact-line { font-size: 11.5px; color: var(--text-grey); line-height: 1.45; }
</style>
</head>
<body>
<main class="stage">
  <section class="business-card business-card--front">
    <div class="brand-block">
      <div class="brand-name"><span class="brand-dot"></span>Brindle Harbor</div>
      <p class="tagline">develop B2B and B2C SAAS based<br>solutions e-commerce portals<br>for companies</p>
    </div>
    <div class="divider"></div>
    <div class="contact-block">
      <p class="person-name">Ravi Kalra</p>
      <div class="accent-lines"><span class="red"></span><span class="blue"></span></div>
      <p class="contact-line">+1-555 014 2290</p>
      <p class="contact-line">info@brindleharbor.in</p>
      <p class="contact-line">www.brindleharbor.com</p>
    </div>
  </section>

  <section class="business-card business-card--back">
    <div class="brand-block">
      <div class="brand-name"><span class="brand-dot"></span>Brindle Harbor</div>
      <p class="tagline">develop B2B and B2C SAAS based<br>solutions e-commerce portals<br>for companies</p>
    </div>
    <div class="divider"></div>
    <div class="contact-block">
      <p class="person-name">Ravi Kalra</p>
      <div class="accent-lines"><span class="red"></span><span class="blue"></span></div>
      <p class="contact-line">+1-555 014 2290</p>
      <p class="contact-line">info@brindleharbor.in</p>
      <p class="contact-line">www.brindleharbor.com</p>
    </div>
  </section>
</main>
</body>
</html>
```